Dentistry

Dentist's personal business card. No logo needed. The card shoul deliver the massage of reliability, professionalism, experience.
Please ad the full brief of the project: down the line it says: the winning look should be precise and pristine NO pictures of Teeth, smiles, instruments etc.

The details to be desplaid are:
Dr. Rob Valdoni
Doctor of Dental Surgery
PHD
Web. Www.drvaldoni.com
Email. Rob@drvaldoni.com
Tel 07731482590
Surgery address. 27Bharwick road London SW4 7QN UK
82 Fenwyn Row London SW3 2HT. Uk

Reason: Decided to make the payment unrefundable in order to get more designers involved.

Requirements
Should not have
• Logo, teeth, smile any sort of instruments.

```html
<!DOCTYPE html>
<html lang="en">
<head>
<meta charset="utf-8">
<title>Dr. Rob Valdoni – Business Card</title>
<link rel="stylesheet" href="https://fonts.googleapis.com/css2?family=Didact+Gothic&family=Montserrat:wght@600&display=swap">
<style>
  :root {
    --backdrop: #eceeee;
    --card: #ffffff;
    --teal: #0e8a84;
    --ink: #2e2e2e;
    --ink-soft: #3a3a3a;
    --on-teal: #ffffff;
  }
  * { margin: 0; padding: 0; box-sizing: border-box; }
  html, body {
    width: 1080px;
    height: 1200px;
    overflow: hidden;
    background: var(--backdrop);
  }
  .canvas {
    position: relative;
    width: 1080px;
    height: 1200px;
  }
  .card {
    position: absolute;
    left: 93px;
    width: 904px;
    height: 503px;
    background: var(--card);
    box-shadow: 0 14px 22px rgba(0, 0, 0, 0.18);
    overflow: hidden;
  }
  .card--front { top: 63px; }
  .card--back { top: 642px; }

  .line {
    position: absolute;
    left: 0;
    width: 100%;
    text-align: center;
    white-space: nowrap;
    transform: translateY(-50%);
    color: var(--ink-soft);
    font-family: "Didact Gothic", sans-serif;
  }
  .name {
    font-family: "Montserrat", sans-serif;
    font-weight: 600;
    color: var(--ink);
  }
  .card--front .name { top: 152px; font-size: 30px; }
  .card--front .title { top: 194px; font-size: 35px; }
  .card--front .degree { top: 238px; font-size: 33px; }

  .card--back .name { top: 68px; font-size: 26px; }
  .card--back .title { top: 102px; font-size: 27px; }
  .card--back .phone { top: 173px; font-size: 27px; }
  .card--back .email { top: 210px; font-size: 27px; }
  .card--back .address-label { top: 264px; font-size: 23px; }
  .card--back .address-one { top: 291px; font-size: 23px; }
  .card--back .address-two { top: 323px; font-size: 23px; }

  .rule {
    position: absolute;
    left: 0;
    width: 100%;
    height: 8px;
    background: var(--teal);
  }
  .band {
    position: absolute;
    left: 0;
    width: 100%;
    bottom: 0;
    height: 132px;
    background: var(--teal);
  }
  .card--front .rule { top: 356px; }
  .card--back .rule { top: 355px; }
  .card--back .band { height: 132px; }

  .website {
    position: absolute;
    left: 0;
    top: 50%;
    width: 100%;
    transform: translateY(-50%);
    text-align: center;
    font-family: "Montserrat", sans-serif;
    font-weight: 600;
    font-size: 30px;
    color: var(--on-teal);
  }
</style>
</head>
<body>
<main class="canvas">
  <section class="card card--front">
    <p class="line name">Dr. Rob Valdoni</p>
    <p class="line title">Doctor of Dental Surgery</p>
    <p class="line degree">PHD</p>
    <div class="rule"></div>
    <div class="band"><p class="website">www.drvaldoni.com</p></div>
  </section>

  <section class="card card--back">
    <p class="line name">Dr. Rob Valdoni</p>
    <p class="line title">Doctor of Dental Surgery PHD</p>
    <p class="line phone">Ph. 07731482590</p>
    <p class="line email">rob@drvaldoni.com</p>
    <p class="line address-label">Surgery address:</p>
    <p class="line address-one">27Bharwick road London SW4 7QN UK</p>
    <p class="line address-two">82 Fenwyn Row London SW3 2HT. Uk</p>
    <div class="rule"></div>
    <div class="band"><p class="website">www.drvaldoni.com</p></div>
  </section>
</main>
</body>
</html>
```